Property investment company needs a letterhead design!

We are a new residential and commercial property investment company. Name of the company is Morvesta Group, LLC. We have a new logo and now we need letterhead! We prefer to have a professional and upscale appearance. We don't have any fixed requirements, so be creative! Thank you for considering this project. We are so excited to see what happens!

Target Market(s)

Professional

Industry/Entity Type

Real Estate Development

```html
<!DOCTYPE html>
<html lang="en">
<head>
<meta charset="utf-8">
<title>Morvesta Group, LLC — Letterhead</title>
<link rel="stylesheet" href="https://fonts.googleapis.com/css2?family=Didact+Gothic&family=Poppins:wght@400;600&display=swap">
<style>
  :root {
    --navy: #13294b;
    --ink: #2a2a2a;
    --text: #3c3c3c;
    --rule: #1d4f91;
    --paper-light: #f3f3f3;
    --paper-dark: #e1e1e1;
    --sign: #d6d6d6;
  }
  * { box-sizing: border-box; margin: 0; padding: 0; }
  html, body { width: 960px; height: 1200px; overflow: hidden; }
  body {
    background: linear-gradient(90deg, var(--paper-light), var(--paper-dark));
    font-family: "Didact Gothic", sans-serif;
    color: var(--text);
  }
  .letterhead { position: relative; width: 960px; height: 1200px; }
  .brand {
    position: absolute; top: 95px; left: 0; width: 100%;
    display: flex; flex-direction: column; align-items: center; gap: 10px;
  }
  .brand-dot {
    width: 46px; height: 46px; border-radius: 50%; background: var(--navy);
  }
  .brand-name {
    font-family: "Poppins", sans-serif; font-weight: 600;
    font-size: 30px; letter-spacing: 2px; color: var(--navy);
    text-transform: uppercase;
  }
  .letter {
    position: absolute; top: 352px; left: 87px; width: 793px;
  }
  .salutation { font-size: 22px; color: var(--ink); margin-bottom: 40px; }
  .body-copy p {
    font-size: 13.2px; line-height: 18.4px; text-align: justify;
    margin-bottom: 18px; color: var(--text);
  }
  .closing { font-size: 13.2px; margin-top: 38px; }
  .signature {
    margin-top: 26px; width: 124px; height: 68px;
    background: var(--sign); border-radius: 4px;
  }
  .footer {
    position: absolute; left: 87px; right: 80px; top: 1104px;
    border-top: 1px solid var(--rule); padding-top: 7px;
    display: flex; justify-content: space-between;
    font-family: "Poppins", sans-serif; font-size: 14.5px; color: var(--ink);
  }
  .contact-row { display: flex; align-items: center; gap: 6px; line-height: 20px; }
  .contact-row svg { width: 11px; height: 11px; fill: var(--navy); flex: none; }
  .contact-row .item { display: inline-flex; align-items: center; gap: 5px; margin-right: 8px; }
  .web { font-weight: 600; color: var(--navy); letter-spacing: 0.6px; line-height: 20px; }
</style>
</head>
<body>
<main class="letterhead">
  <header class="brand">
    <span class="brand-dot"></span>
    <span class="brand-name">Morvesta Group, LLC</span>
  </header>

  <section class="letter">
    <p class="salutation">Dear Mr. Hollis,</p>
    <div class="body-copy">
      <p>Lorem ipsum dolor sit amet, consectetur adipiscing elit. Donec orci purus, luctus vitae dignissim eu, iaculis sed purus. Vivamus faucibus, ipsum nec aliquet viverra, leo mauris condimentum ligula, sit amet sagittis enim ligula quis arcu. Nam egestas tortor id nisi porttitor mattis. In tortor ante, ultricies in suscipit a, tempus non massa. Vivamus et auctor mi. Fusce vel massa nulla. Phasellus nec eros mauris, et scelerisque orci.</p>
      <p>Donec malesuada orci vitae nulla accumsan porta a id massa. Quisque accumsan iaculis magna sit amet fringilla. Maecenas consequat, magna eget tincidunt semper, odio nibh rutrum mi, id feugiat ante nisi eu risus. Vestibulum nunc orci, rhoncus a placerat in, ultricies in mi. Cras mattis varius eros, vel fringilla nisi suscipit eget. Quisque scelerisque sagittis nulla at porttitor.</p>
      <p>Sed id augue vitae urna euismod commodo aliquet a quam. Pellentesque arcu velit, cursus et malesuada ut, consequat et diam. Nullam erat sem, rhoncus id ullamcorper vitae, rhoncus et arcu. In ultricies ultricies nulla, ut rutrum nisi iaculis at. Donec eu magna a metus ornare faucibus. Fusce aliquet faucibus ultricies. Morbi semper, est id tincidunt gravida, sem arcu adipiscing lacus, ac bibendum nulla leo eu purus. Quisque nec diam sed risus consectetur a ccumsan quis quis nibh. Vestibulum id purus lorem.</p>
      <p>It is a long established fact that a reader will be distracted by the readable content of a page when looking at its layout. The point of using Lorem Ipsum is that it has a more-or-less normal distribution of letters, as opposed to using 'Content here, content here', making it look like readable English. Many desktop publishing packages</p>
    </div>
    <p class="closing">Sincerely,</p>
    <div class="signature" role="img" aria-label="Handwritten signature of the letter's sender"></div>
  </section>

  <footer class="footer">
    <div class="contact">
      <div class="contact-row">
        <span class="item">
          <svg viewBox="0 0 24 24" aria-hidden="true"><path d="M6.6 10.8a15.1 15.1 0 0 0 6.6 6.6l2.2-2.2c.3-.3.7-.4 1-.2 1.1.4 2.3.6 3.6.6.6 0 1 .4 1 1V20c0 .6-.4 1-1 1A17 17 0 0 1 3 4c0-.6.4-1 1-1h3.5c.6 0 1 .4 1 1 0 1.3.2 2.5.6 3.6.1.3 0 .7-.2 1z"/></svg>
          555-204-7731
        </span>
        <span class="item">
          <svg viewBox="0 0 24 24" aria-hidden="true"><path d="M6 3h12v5H6zM3 9h18v9h-3v3H6v-3H3zm5 7v3h8v-3z"/></svg>
          555-204-7732
        </span>
        <span class="item">
          <svg viewBox="0 0 24 24" aria-hidden="true"><path d="M2 5h20v14H2zm2 2v.5l8 5 8-5V7z"/></svg>
          info@morvesta.com
        </span>
      </div>
      <div class="contact-row">
        <span class="item">
          <svg viewBox="0 0 24 24" aria-hidden="true"><path d="M12 2a7 7 0 0 0-7 7c0 5 7 13 7 13s7-8 7-13a7 7 0 0 0-7-7zm0 9.5A2.5 2.5 0 1 1 12 6.5a2.5 2.5 0 0 1 0 5z"/></svg>
          1420 Larchmont Way, Fairbanks, Alaska 99701
        </span>
      </div>
    </div>
    <div class="web">www.Morvesta.com</div>
  </footer>
</main>
</body>
</html>
```